New London Job Board - Business Card Required

Dear All,

I own Quintaro Limited, which in turn owns the website:
www.brambletopfield.com

I want all of you wonderful creative people to come up with a slick, and awesome business card design that incorporates the logo on the site, and some colouring and design elements from it.

You have free reign in how you go about doing this, I won't be giving my contact details on this platform, but the winner will be asked to redesign based on my contact details which I will supply at the end.

I need the design to be completed within 5 days. I need the final print copies of the business cards by the 25th November, so unfortunately it's a bit of a rush to get these designs ready.

Any questions, please ask.

Thank you

Thank you all for your hard work and exceptional designs provided. I do have to pick one, so I have a very clear idea of which one this is, however I will wait one further day until the competition closes to be fair to all those have submitted, or are in the process of submitting. I wish you all the best and thank you again for your dedication.

```html
<!DOCTYPE html>
<html lang="en">
<head>
<meta charset="utf-8">
<title>Brambletop Field – Business Card</title>
<link href="https://fonts.googleapis.com/css2?family=Lato:wght@400;700&display=swap" rel="stylesheet">
<style>
  :root {
    --stage: #e9e6e1;
    --card-black: #0d0d0d;
    --card-shade: #1b1b1b;
    --gold-light: #f3d77a;
    --gold: #c99a2e;
    --gold-deep: #8a6414;
    --text-gold: #d9ad45;
  }
  * { box-sizing: border-box; margin: 0; padding: 0; }
  html, body { width: 1200px; height: 1023px; overflow: hidden; }
  body {
    background: var(--stage);
    font-family: "Lato", Arial, sans-serif;
    position: relative;
  }
  .card {
    position: absolute;
    width: 640px;
    height: 366px;
    border-radius: 4px;
    overflow: hidden;
    box-shadow: 0 10px 28px rgba(0,0,0,.28);
  }
  .card-front { left: 50px; top: 80px; }
  .card-back { left: 510px; top: 560px; }
  .card-texture {
    position: absolute; inset: 0;
    background: radial-gradient(ellipse at 40% 45%, var(--card-shade), var(--card-black) 75%);
  }
  .gold-wave { position: absolute; inset: 0; }
  .brand {
    position: absolute;
    color: var(--text-gold);
    font-weight: 700;
    text-transform: uppercase;
    letter-spacing: 3px;
    display: flex;
    align-items: center;
    gap: 12px;
  }
  .brand-dot {
    width: 14px; height: 14px; border-radius: 50%;
    background: var(--text-gold);
    flex: none;
  }
  .card-front .brand { left: 36px; top: 168px; font-size: 21px; }
  .card-back .brand {
    left: 0; right: 0; top: 0; bottom: 0;
    justify-content: center; font-size: 34px; letter-spacing: 5px;
  }
  .card-back .brand-dot { width: 20px; height: 20px; }
  .contact {
    position: absolute; left: 300px; top: 34px;
    color: var(--text-gold);
  }
  .person-name { font-size: 21px; letter-spacing: 2px; font-weight: 400; text-transform: uppercase; }
  .person-role { font-size: 12px; margin-top: 2px; margin-left: 22px; }
  .contact-list { list-style: none; margin-top: 22px; font-size: 12.5px; }
  .contact-list li { display: flex; align-items: center; gap: 9px; margin-bottom: 7px; }
  .contact-list svg { width: 13px; height: 13px; flex: none; }
  .address { margin-top: 20px; margin-left: 22px; font-size: 12.5px; line-height: 1.75; }
</style>
</head>
<body>

<section class="card card-front" aria-label="Card front">
  <div class="card-texture" role="img" aria-label="Black card with subtle dark floral damask pattern"></div>
  <svg class="gold-wave" viewBox="0 0 640 366" preserveAspectRatio="none" aria-hidden="true">
    <defs>
      <linearGradient id="goldFill" x1="0" y1="1" x2="1" y2="0">
        <stop offset="0" stop-color="var(--gold-deep)"/>
        <stop offset="0.45" stop-color="var(--gold-light)"/>
        <stop offset="1" stop-color="var(--gold)"/>
      </linearGradient>
    </defs>
    <path d="M640 0 C590 150 470 270 245 366 L640 366 Z" fill="url(#goldFill)"/>
    <path d="M640 40 C600 170 500 280 330 366 L640 366 Z" fill="#000" opacity=".25"/>
    <path d="M632 0 C585 140 460 262 232 366" fill="none" stroke="#000" stroke-width="6"/>
    <path d="M618 60 C585 150 520 220 430 270" fill="none" stroke="var(--gold-light)" stroke-width="2"/>
  </svg>

  <div class="brand"><span class="brand-dot"></span>Brambletop Field</div>

  <div class="contact">
    <h1 class="person-name">Idris Halloway</h1>
    <p class="person-role">Managing Director</p>
    <ul class="contact-list">
      <li>
        <svg viewBox="0 0 14 14"><rect x="4" y="1" width="6" height="12" rx="1.5" fill="var(--text-gold)"/></svg>
        0700 000 1234
      </li>
      <li>
        <svg viewBox="0 0 14 14"><rect x="1" y="3" width="12" height="8" fill="var(--text-gold)"/><path d="M1 3 L7 8 L13 3" fill="none" stroke="#000" stroke-width="1"/></svg>
        contact@brambletopfield.com
      </li>
      <li>
        <svg viewBox="0 0 14 14"><circle cx="7" cy="7" r="6" fill="var(--text-gold)"/><path d="M1 7 H13 M7 1 C4 4 4 10 7 13 M7 1 C10 4 10 10 7 13" fill="none" stroke="#000" stroke-width=".8"/></svg>
        www.brambletopfield.com
      </li>
    </ul>
    <p class="address">BRAMBLETOP FIELD<br>17 Larkspur Row, Fenwick,<br>London, E9 4QT</p>
  </div>
</section>

<section class="card card-back" aria-label="Card back">
  <div class="card-texture" role="img" aria-label="Black card with subtle dark floral damask pattern"></div>
  <div class="brand"><span class="brand-dot"></span>Brambletop Field</div>
</section>

</body>
</html>
```